Rising Paths Web Design

I am starting a new company that will provide LIFE COACHING services - I have tried to design a website, but it's too complicated. Right now, it's just me - I'm the only person that will provide services through the website - I have used artmarket to purchase a logo (see below). I want to be able to update the website myself, but need a template - basic design. Because I am not technologically savvy enough to explain in words - I basically want to have a website that will provide basic information about my services (coaching), a page about me and my background, hopefully scheduling possibilities, and testimonials — also a page for writing/blogs. I bought a website through NetHarbor - so when I have a template, I guess I”d use that - but maybe I’ll need to work with a designer to actually get it up on the internet. I have a head shot that I’ll upload, too.
Target Market(s)
Clients from the independent (private school) world - teachers, administrators
Number of Pages Required
4 page
Look and feel
Each slider illustrates characteristics of the customer's brand and the style your logo design should communicate.

```html
<!DOCTYPE html>
<html lang="en">
<head>
<meta charset="utf-8">
<title>Rising Paths Coaching</title>
<link href="https://fonts.googleapis.com/css2?family=Cormorant+Garamond:wght@500;600&family=Jost:wght@400;500;600&display=swap" rel="stylesheet">
<style>
:root{
  --teal:#0ea38a;
  --ink:#111111;
  --text:#4a4a4a;
  --muted:#777777;
  --grey:#f4f4f4;
  --line:#e4e4e4;
  --white:#ffffff;
  --photo-warm:#b79a86;
  --photo-cool:#9aa4a8;
}
*{box-sizing:border-box;margin:0;padding:0}
html,body{width:1200px;height:4737px;overflow:hidden;background:var(--white)}
body{font-family:'Jost',sans-serif;color:var(--text);position:relative}
.page{position:relative;width:1200px;height:4737px;overflow:hidden}
.abs{position:absolute}
.serif{font-family:'Cormorant Garamond',serif;color:var(--ink);font-weight:600}
.eyebrow{font-size:13px;font-weight:500;color:var(--teal);text-transform:uppercase;letter-spacing:.3px;display:flex;align-items:center;gap:12px}
.eyebrow::before{content:"";width:30px;height:1px;background:var(--teal)}
.eyebrow.center::after{content:"";width:0}
.photo{position:absolute}
.btn-outline{position:absolute;border:2px solid var(--ink);display:flex;align-items:center;justify-content:center;font-size:13px;font-weight:600;color:var(--ink);text-transform:uppercase}
/* header */
.brand{position:absolute;left:100px;top:16px;width:140px;height:112px;display:flex;align-items:center;gap:10px}
.brand-mark{width:14px;height:14px;border-radius:50%;background:var(--teal);flex:none}
.brand-name{font-family:'Cormorant Garamond',serif;font-weight:600;font-size:18px;color:var(--ink);line-height:1.05;text-transform:uppercase}
.nav{position:absolute;left:327px;top:60px;font-size:13px;color:var(--muted);display:flex;gap:8px}
.nav a{color:var(--muted);text-decoration:none}
.nav a.active{color:var(--teal)}
.hero-band{position:absolute;left:790px;top:0;width:410px;height:777px;background:var(--teal)}
.contact{position:absolute;left:921px;top:52px;display:flex;gap:16px;color:var(--white);font-size:12px;line-height:1.5}
.contact b{font-weight:600}
.hero-photo{left:86px;top:143px;width:1028px;height:541px;background:linear-gradient(100deg,#6b5444 0%,#8e7460 35%,#c9b8a8 60%,#5d6660 100%)}
.hero-card{position:absolute;left:132px;top:213px;width:452px;height:423px;background:var(--white);padding:54px 42px}
.hero-card h1{font-size:58px;line-height:1.17;margin-top:20px}
.btn-dark{position:absolute;left:42px;top:316px;width:186px;height:56px;background:var(--ink);color:var(--white);font-size:13px;font-weight:600;display:flex;align-items:center;justify-content:center}
.socials{position:absolute;left:35px;top:352px;display:flex;flex-direction:column;gap:42px}
.socials span{width:11px;height:11px;background:var(--teal);display:block}
/* services */
.service{position:absolute;top:980px;width:326px;height:351px}
.service .photo{left:0;top:0;width:326px;height:215px}
.service-box{position:absolute;left:24px;top:213px;width:278px;height:138px;background:var(--white);padding:28px 26px;box-shadow:0 4px 18px rgba(0,0,0,.06)}
.service-box.on{background:var(--teal)}
.service-box.on .eyebrow,.service-box.on h3{color:var(--white)}
.service-box.on .eyebrow::before{background:var(--white)}
.service-box h3{font-size:24px;font-weight:500;line-height:1.2;margin-top:14px}
/* story */
.story p{font-size:13.5px;line-height:1.75}
/* testimonials */
.t-card{position:absolute;top:2377px;width:245px;height:233px;border:1px solid #444;padding:32px 26px;color:#ddd;font-size:14px;line-height:1.6}
.stars{color:var(--teal);font-size:20px;letter-spacing:1px;margin-bottom:10px}
.person{position:absolute;top:2640px;display:flex;align-items:center;gap:14px;color:var(--white);font-size:14px;font-weight:500}
.person small{display:block;font-size:11px;font-weight:400;color:#ccc}
.avatar{width:58px;height:58px;border-radius:50%;background:linear-gradient(#c49a86,#8a6a5a)}
/* schedule */
.event{position:absolute;top:3010px;width:236px}
.event .icon{width:70px;height:70px;border-radius:50%;background:rgba(14,163,138,.18)}
.event .num{position:absolute;right:0;top:88px;font-size:36px;font-weight:600;color:#d8d8d8}
.event .date{position:absolute;top:150px;font-size:13px;color:var(--teal);display:flex;gap:10px;align-items:center}
.event h4{position:absolute;top:182px;font-size:23px;font-weight:500;line-height:1.3}
.link{font-size:12px;font-weight:500;color:var(--teal);text-transform:uppercase;text-decoration:underline}
.event .link{position:absolute;top:272px}
/* blog */
.post{position:absolute;top:3608px;width:326px;height:404px;background:var(--white);border:1px solid var(--line)}
.post .photo{left:19px;top:22px;width:288px;height:189px}
.badge{position:absolute;left:210px;top:183px;width:62px;height:60px;background:var(--teal);color:var(--white);font-weight:600;text-align:center;line-height:1.1;padding-top:9px;font-size:20px}
.badge small{display:block;font-size:14px}
.post .by{position:absolute;left:28px;top:242px;color:var(--teal);font-size:16px;display:flex;gap:8px;align-items:center}
.post p{position:absolute;left:28px;top:280px;font-family:'Cormorant Garamond',serif;color:var(--ink);font-size:19px;font-weight:500;line-height:1.3}
.post .link{position:absolute;left:28px;top:355px}
/* newsletter */
.news{position:absolute;left:0;top:4112px;width:1200px;height:209px;background:var(--teal)}
.news .eyebrow{color:var(--white)}
.news .eyebrow::before{background:var(--white)}
/* footer */
.f-links a{position:absolute;font-size:13px;color:#555;text-transform:uppercase;text-decoration:none}
.f-social{position:absolute;top:4425px;width:38px;height:38px;border:1px solid var(--teal);border-radius:50%}
</style>
</head>
<body>
<div class="page">

<!-- header -->
<div class="hero-band"></div>
<div class="brand"><span class="brand-mark"></span><span class="brand-name">Rising Paths<br><small style="font-size:11px;color:var(--teal)">Coaching</small></span></div>
<nav class="nav"><a class="active">Home</a>|<a>About Me</a>|<a>My Services</a>|<a>Schedule</a>|<a>Testimonials</a>|<a>Blog</a></nav>
<svg class="abs" style="left:875px;top:60px" width="20" height="20" viewBox="0 0 20 20" fill="none" stroke="#fff" stroke-width="2"><circle cx="8" cy="8" r="6"/><path d="M13 13l5 5"/></svg>
<div class="contact">
  <svg width="38" height="34" viewBox="0 0 38 34"><rect x="0" y="0" width="28" height="20" rx="2" fill="#fff"/><path d="M5 20l0 8 8-8z" fill="#fff"/><rect x="10" y="10" width="28" height="18" rx="2" fill="#fff" stroke="#0ea38a" stroke-width="2"/><path d="M16 17h18M16 22h14" stroke="#0ea38a" stroke-width="2"/></svg>
  <div><b>Have Any Questions?</b><br>+ 01555 214 77</div>
</div>

<!-- hero -->
<div class="photo hero-photo" role="img" aria-label="Portrait of a smiling coach in a white shirt"></div>
<div class="hero-card">
  <div class="eyebrow">Rising Paths Coaching</div>
  <h1 class="serif">“Always Push Yourself to the Next Level”</h1>
  <div class="btn-dark">GET FREE SESSION</div>
</div>
<div class="socials"><span></span><span></span><span></span></div>
<svg class="abs" style="left:8px;top:650px" width="112" height="96"><defs><pattern id="dots" width="14" height="14" patternUnits="userSpaceOnUse"><circle cx="2" cy="2" r="1.3" fill="#bbb"/></pattern></defs><rect width="112" height="96" fill="url(#dots)"/></svg>

<!-- services -->
<div class="abs eyebrow" style="left:86px;top:876px">My Services</div>
<h2 class="abs serif" style="left:86px;top:896px;font-size:46px;font-weight:500">My Most Beloved Services</h2>
<div class="btn-outline" style="left:928px;top:879px;width:186px;height:58px;border-width:1px">View All Services</div>

<div class="service" style="left:86px"><div class="photo" role="img" aria-label="Young woman smiling at a workshop" style="background:linear-gradient(#a68b78,#e6dcd2)"></div>
  <div class="service-box"><div class="eyebrow">One to One</div><h3 class="serif">Personal Sessions and Workshops</h3></div></div>
<div class="service" style="left:437px"><div class="photo" role="img" aria-label="Clipboard with speaking notes and a cup of coffee" style="background:linear-gradient(120deg,#f3c9c2,#f4ede8)"></div>
  <div class="service-box on"><div class="eyebrow">Public</div><h3 class="serif">Public Program for Individuals and Teams</h3></div></div>
<div class="service" style="left:788px"><div class="photo" role="img" aria-label="Hands holding a tablet on a desk" style="background:linear-gradient(120deg,#c9cfcf,#e8ecec)"></div>
  <div class="service-box"><div class="eyebrow">Online</div><h3 class="serif">Learn Secrets to Peak Performance</h3></div></div>

<!-- story -->
<div class="abs" style="left:0;top:1432px;width:261px;height:298px;background:var(--grey)"></div>
<div class="abs" style="left:498px;top:1529px;width:64px;height:381px;background:var(--teal)"></div>
<div class="photo" role="img" aria-label="Coach standing by a tree with arms crossed" style="left:86px;top:1492px;width:412px;height:454px;background:linear-gradient(110deg,#6e5a4a,#a89484 50%,#7a6a5c)"></div>
<div class="story abs" style="left:614px;top:1540px;width:500px">
  <div class="eyebrow">My Story</div>
  <h2 class="serif" style="font-size:46px;font-weight:500;line-height:1.28;margin-top:16px">Hello, I’m Maren<br>Holt</h2>
  <p style="margin-top:14px">Lorem ipsum dolor sit amet, consectetur adipiscing elit. Suspendisse sed interdum leo. Sed pretium eleifend risus nec sagittis. Quisque laoreet purus aliquam, mattis metus vitae, ornare tellus. Curabitur bibendum facilisis mauris, sed varius enim pretium ut. Mauris bibendum ex erat, nec volutpat est vulputate non.</p>
</div>
<div class="btn-outline" style="left:614px;top:1836px;width:187px;height:59px">Read My Story</div>

<!-- testimonials -->
<div class="photo" role="img" aria-label="Two women talking on a sofa during a coaching session" style="left:0;top:2048px;width:599px;height:742px;background:linear-gradient(120deg,#cfc7bd,#9b8f84 55%,#3a3430)"></div>
<div class="abs" style="left:599px;top:2048px;width:601px;height:112px;background:#8f8a86"></div>
<div class="abs" style="left:836px;top:2048px;width:364px;height:112px;background:var(--teal)"></div>
<div class="abs" style="left:599px;top:2160px;width:601px;height:630px;background:#000"></div>
<div class="abs eyebrow" style="left:645px;top:2210px">Clients Testimonials</div>
<h2 class="abs serif" style="left:645px;top:2232px;font-size:46px;font-weight:500;color:#fff;line-height:1.28">Satisfied Users Over<br>The Globel</h2>
<div class="t-card" style="left:645px"><div class="stars">★★★★★</div>Donec pellentesque laoreet quam. Praesent maximus ligula ornare imperdiet placerat. Donec ut finibus elit. Nulla consectetur convallis suscipit.</div>
<div class="t-card" style="left:912px"><div class="stars">★★★★★</div>Donec pellentesque laoreet quam. Praesent maximus ligula ornare imperdiet placerat. Donec ut finibus elit. Nulla consectetur convallis suscipit.</div>
<div class="person" style="left:688px"><div class="avatar" role="img" aria-label="Client portrait"></div><div>Nora Fielding<small>CEO at Lumwell</small></div></div>
<div class="person" style="left:954px"><div class="avatar" role="img" aria-label="Client portrait"></div><div>Nora Fielding<small>CEO at Lumwell</small></div></div>
<svg class="abs" style="left:880px;top:2727px" width="46" height="8"><rect x="0" width="8" height="8" fill="#0ea38a"/><rect x="19" width="8" height="8" fill="#fff"/><rect x="38" width="8" height="8" fill="#fff"/></svg>

<!-- schedule -->
<div class="abs eyebrow" style="left:540px;top:2890px">Schedule</div>
<h2 class="abs serif" style="left:0;top:2910px;width:1200px;text-align:center;font-size:46px;font-weight:500">Upcoming Schedule</h2>
<div class="event" style="left:86px"><div class="icon" role="img" aria-label="Goals icon"></div><div class="num">01</div><div class="date"><svg width="16" height="16" fill="none" stroke="#0ea38a" stroke-width="1.6"><rect x="1" y="3" width="14" height="12"/><path d="M1 7h14M5 1v4M11 1v4"/></svg>July 30, 2022 | 12:00 PM</div><h4 class="serif">Ut lobortis in nunc vel auctor. Etiam id</h4><a class="link">View Details</a></div>
<div class="event" style="left:349px"><div class="icon" role="img" aria-label="Care icon"></div><div class="num">02</div><div class="date"><svg width="16" height="16" fill="none" stroke="#0ea38a" stroke-width="1.6"><rect x="1" y="3" width="14" height="12"/><path d="M1 7h14M5 1v4M11 1v4"/></svg>July 30, 2022 | 12:00 PM</div><h4 class="serif">Ut lobortis in nunc vel auctor. Etiam id</h4><a class="link">View Details</a></div>
<div class="event" style="left:614px"><div class="icon" role="img" aria-label="Mentor icon"></div><div class="num">03</div><div class="date"><svg width="16" height="16" fill="none" stroke="#0ea38a" stroke-width="1.6"><rect x="1" y="3" width="14" height="12"/><path d="M1 7h14M5 1v4M11 1v4"/></svg>July 30, 2022 | 12:00 PM</div><h4 class="serif">Ut lobortis in nunc vel auctor. Etiam id</h4><a class="link">View Details</a></div>
<div class="event" style="left:879px"><div class="icon" role="img" aria-label="Support icon"></div><div class="num">04</div><div class="date"><svg width="16" height="16" fill="none" stroke="#0ea38a" stroke-width="1.6"><rect x="1" y="3" width="14" height="12"/><path d="M1 7h14M5 1v4M11 1v4"/></svg>July 30, 2022 | 12:00 PM</div><h4 class="serif">Ut lobortis in nunc vel auctor. Etiam id</h4><a class="link">View Details</a></div>

<!-- blog -->
<div class="abs" style="left:0;top:3400px;width:1200px;height:712px;background:#f7f7f7"></div>
<div class="abs eyebrow" style="left:540px;top:3496px">Our Blog</div>
<h2 class="abs serif" style="left:0;top:3514px;width:1200px;text-align:center;font-size:46px;font-weight:500">Latest News &amp; Updates</h2>
<div class="post" style="left:86px"><div class="photo" role="img" aria-label="Notebook and coffee on a table" style="background:linear-gradient(120deg,#3a2a20,#e9e6e0 55%)"></div><div class="badge">31<small>JULY</small></div><div class="by"><svg width="16" height="16" fill="#0ea38a"><circle cx="8" cy="5" r="4"/><path d="M0 16c0-5 16-5 16 0z"/></svg>By Admin</div><p>Lorem ipsum dolor sit amet, consectetur adipiscing</p><a class="link">Read More</a></div>
<div class="post" style="left:437px"><div class="photo" role="img" aria-label="Two people in a consultation" style="background:linear-gradient(120deg,#dfe6ec,#9eaab4 60%,#eef1f3)"></div><div class="badge">31<small>JULY</small></div><div class="by"><svg width="16" height="16" fill="#0ea38a"><circle cx="8" cy="5" r="4"/><path d="M0 16c0-5 16-5 16 0z"/></svg>By Admin</div><p>Lorem ipsum dolor sit amet, consectetur adipiscing</p><a class="link">Read More</a></div>
<div class="post" style="left:788px"><div class="photo" role="img" aria-label="Person climbing steps outdoors" style="background:linear-gradient(#e8c9b4,#d58c94 60%,#cfa79f)"></div><div class="badge">31<small>JULY</small></div><div class="by"><svg width="16" height="16" fill="#0ea38a"><circle cx="8" cy="5" r="4"/><path d="M0 16c0-5 16-5 16 0z"/></svg>By Admin</div><p>Lorem ipsum dolor sit amet, consectetur adipiscing</p><a class="link">Read More</a></div>

<!-- newsletter -->
<div class="news">
  <div class="abs eyebrow" style="left:86px;top:60px">Keep Up to Date With Advantage</div>
  <h2 class="abs serif" style="left:86px;top:84px;font-size:46px;font-weight:500;color:#fff">Subscribe to Our Newsletter</h2>
  <div class="abs" style="left:700px;top:71px;width:296px;height:61px;background:#fff;font-size:13px;color:#777;padding:21px 24px">Enter Email</div>
  <div class="abs" style="left:996px;top:71px;width:118px;height:61px;background:var(--ink);color:#fff;font-size:13px;font-weight:600;display:flex;align-items:center;justify-content:center">SUBSCRIBE</div>
</div>

<!-- footer -->
<div class="abs" style="left:86px;top:4450px;display:flex;align-items:center;gap:8px"><span class="brand-mark" style="width:10px;height:10px;border-radius:50%;background:var(--teal)"></span><span class="brand-name" style="font-size:15px">Rising Paths</span></div>
<div class="abs" style="left:86px;top:4530px;font-size:13px;line-height:2.95;color:#444">hello@risingpaths.example<br>(555) 214 7780<br>Enter your address here</div>
<div class="f-links">
  <a style="left:531px;top:4424px">My Story</a><a style="left:531px;top:4471px">My Schedule</a><a style="left:531px;top:4519px">Services</a>
  <a style="left:700px;top:4424px">Testimonials</a><a style="left:700px;top:4471px">News</a><a style="left:700px;top:4519px">Contact</a>
  <a style="left:866px;top:4424px">FAQs</a><a style="left:866px;top:4471px">T &amp; C</a>
</div>
<div class="f-social" style="left:967px"></div><div class="f-social" style="left:1021px"></div><div class="f-social" style="left:1075px"></div>
<div class="abs" style="left:86px;top:4674px;font-size:12px;color:#555">Copyright 2022.All right reserved.</div>
<div class="abs" style="left:956px;top:4674px;font-size:12px;color:#555;word-spacing:4px">Privacy Policy &nbsp;&nbsp;&nbsp; Sitemap</div>

</div>
</body>
</html>
```